Upscale Adult website

Looking for the design mock-up of an intuitive, professional and upscale adult website. No HTML necessary, just a competent design theme. The site will be category centric. This means that finding and selecting a specific categories in any easy and intuitive way is vey important. Looking for mock-up of Home Page, a Category Screen, and the Login Screen. The site should have a fun feel but be more corporate rather than "porn." There must also be free space where ads will appear. See attached file for complete list of functionality and necessary icons for the Home Screen.

Industry/Entity Type

Adult

```html
<!DOCTYPE html>
<html lang="en">
<head>
<meta charset="utf-8">
<title>Velvet Reel — Home</title>
<link rel="stylesheet" href="https://fonts.googleapis.com/css2?family=Open+Sans:wdth,wght@75..100,400..700&display=swap">
<style>
:root{
  --page-bg:#262626;
  --page-light:#3a3a3a;
  --page-dark:#141414;
  --panel:#0c0c0c;
  --panel-edge:#1e1e1e;
  --nav-text:#bdbdbd;
  --white:#ffffff;
  --accent:#e4202a;
  --muted:#6f6f6f;
  --thumb-border:#6a6a6a;
  --footer-bg:#000;
  --footer-text:#8a8a8a;
}
*{box-sizing:border-box;margin:0;padding:0}
html,body{width:902px;height:1200px;overflow:hidden}
body{
  position:relative;
  font-family:"Open Sans",Arial,sans-serif;
  background:var(--page-bg);
  color:var(--white);
}
.wallpaper{
  position:absolute;left:0;top:0;width:902px;height:1100px;
  background:
    radial-gradient(ellipse 60% 45% at 50% 45%, rgba(255,255,255,.06), rgba(255,255,255,0) 70%),
    radial-gradient(ellipse at 50% 50%, var(--page-light) 0, var(--page-bg) 55%, var(--page-dark) 100%);
}

/* ---------- header ---------- */
.top-bar{
  position:absolute;left:100px;top:0;width:702px;height:34px;
  background:linear-gradient(#2b2b2b,#151515);
  border-radius:0 0 4px 4px;
}
.main-nav{font-size:12px;color:var(--nav-text)}
.main-nav a{position:absolute;top:10px;color:inherit;text-decoration:none;text-transform:uppercase;white-space:nowrap}
.main-nav .has-menu::after{
  content:"";position:absolute;left:50%;top:15px;margin-left:-3px;
  border:4px solid transparent;border-top-color:var(--nav-text);
}
.icon-btn{position:absolute;top:9px;width:17px;height:17px;border-radius:50%;background:#d8d8d8;display:flex;align-items:center;justify-content:center}
.login{position:absolute;top:8px;font-size:8px;color:#777}
.login .field{position:absolute;top:0;height:14px;border-radius:7px;background:#050505;padding:1px 8px;font-size:8px;color:#777}
.login .register{position:absolute;left:119px;top:14px;font-size:6px;color:#9a9a9a;white-space:nowrap}

.brand{
  position:absolute;left:100px;top:34px;width:130px;height:62px;
  background:#0a0a0a;border-radius:0 0 6px 6px;
  font-size:12px;font-weight:700;display:flex;align-items:center;justify-content:center;
}
.category-strip{position:absolute;left:230px;top:34px;width:572px;height:56px;background:#050505}
.category-tile{
  position:absolute;top:6px;width:48px;height:44px;border:1px solid #555;
  background:linear-gradient(135deg,#b39a8c,#5a4a44);
}
.category-tile.dark{background:linear-gradient(135deg,#2a2a2a,#050505)}
.category-tile.warm{background:linear-gradient(135deg,#d8a86a,#6f7f9a)}
.category-tile span{
  position:absolute;left:0;right:0;bottom:0;min-height:12px;background:rgba(255,255,255,.88);
  color:#111;font-size:5.5px;font-weight:700;text-align:center;line-height:6px;padding:1px 0;
  display:flex;align-items:center;justify-content:center;
}
.strip-next{position:absolute;left:555px;top:20px}

/* ---------- sections ---------- */
.panel{position:absolute;background:var(--panel);box-shadow:0 0 18px rgba(0,0,0,.6)}
.panel-title{position:absolute;left:45px;font-size:12px;font-weight:600;text-transform:uppercase}
.featured-top{left:118px;top:114px;width:666px;height:164px;background:linear-gradient(#101010,#050505 60%,#161616)}
.recent{left:100px;top:300px;width:702px;height:594px;border-radius:6px;border:1px solid var(--panel-edge)}
.featured-bottom{left:118px;top:912px;width:666px;height:168px;background:linear-gradient(#101010,#050505 60%,#161616)}
.featured-top .panel-title,.featured-bottom .panel-title{left:27px}

.arrow{position:absolute;width:16px;height:28px}
.row{position:absolute;display:flex;gap:10px}

.video-card{width:114px}
.thumb{
  position:relative;width:114px;height:114px;border:2px solid var(--thumb-border);
  display:flex;align-items:center;justify-content:center;
}
.thumb.embrace{background:linear-gradient(135deg,#cbb9ae,#7a6258 60%,#3a2f2b)}
.thumb.night{background:linear-gradient(135deg,#1c1c1c,#000 70%)}
.thumb.close{background:linear-gradient(135deg,#e0d4cc,#9b8478 55%,#efe6df)}
.thumb.beach{background:linear-gradient(160deg,#6f86aa,#d7a765 55%,#2b2b2b)}
.thumb .play{width:22px;height:24px}
.thumb .play-label{position:absolute;bottom:6px;left:0;right:0;text-align:center;font-size:11px;font-weight:600;color:var(--accent)}
.video-title{margin-top:5px;font-size:11.5px;line-height:14px;color:var(--accent);font-stretch:90%;letter-spacing:-.1px}
.video-meta{
  display:flex;justify-content:space-between;align-items:center;
  font-size:10.5px;font-stretch:85%;letter-spacing:-.1px;color:var(--muted);margin-top:-1px;white-space:nowrap
}
.likes{display:flex;align-items:center;gap:2px}
.likes i{width:11px;height:11px;border-radius:50%;background:var(--accent);display:inline-flex;align-items:center;justify-content:center}

.pagination{position:absolute;left:294px;top:857px;display:flex;gap:7px;align-items:center}
.pagination span{
  width:24px;height:24px;border-radius:50%;border:2px solid #bdbdbd;
  display:flex;align-items:center;justify-content:center;font-size:13px;color:#eee;
}
.pagination .current{border-color:#444;color:#555;background:#1a1a1a}
.pagination .gap{width:auto;border:0;letter-spacing:1px;font-weight:700}

/* ---------- footer ---------- */
.site-footer{position:absolute;left:0;top:1100px;width:902px;height:100px;background:var(--footer-bg)}
.footer-col{position:absolute;top:14px;font-size:8.5px;line-height:11.4px;color:var(--footer-text)}
.footer-col h4{font-size:9px;font-weight:700;color:#eee;margin-bottom:4px}
.copyright{position:absolute;left:0;right:0;top:88px;text-align:center;font-size:6.5px;color:#ddd;font-weight:600}
</style>
</head>
<body>

<div class="wallpaper" role="img" aria-label="Dark grey damask wallpaper texture"></div>

<header>
  <div class="top-bar">
    <nav class="main-nav">
      <a style="left:15px">Home</a>
      <a style="left:74px">Highest Rated</a>
      <a style="left:181px">Most Viewed</a>
      <a style="left:270px">Recently Added</a>
      <a class="has-menu" style="left:380px">Categories</a>
    </nav>
    <span class="icon-btn" style="left:464px">
      <svg width="9" height="8" viewBox="0 0 10 9"><path d="M5 9 1 5A2.4 2.4 0 0 1 5 1.6 2.4 2.4 0 0 1 9 5Z" fill="#111"/></svg>
    </span>
    <span class="icon-btn" style="left:492px">
      <svg width="9" height="9" viewBox="0 0 10 10"><path d="M5 1 2 4h2v3h2V4h2ZM2 8h6v1H2Z" fill="#111"/></svg>
    </span>
    <div class="login" style="left:524px">
      <span class="field" style="left:0;width:70px">name</span>
      <span class="field" style="left:81px;width:67px">password <b style="position:absolute;right:6px;color:#aaa">&gt;</b></span>
      <span class="register">or register</span>
    </div>
  </div>

  <div class="brand">PLACE LOGO HERE</div>

  <div class="category-strip">
    <div class="category-tile" style="left:8px" role="img" aria-label="Category preview"><span>ASIAN</span></div>
    <div class="category-tile dark" style="left:57px" role="img" aria-label="Category preview"><span>GIRL ON<br>GIRL</span></div>
    <div class="category-tile" style="left:106px" role="img" aria-label="Category preview"><span>TWO ON<br>ONE</span></div>
    <div class="category-tile warm" style="left:155px" role="img" aria-label="Category preview"><span>LATINA</span></div>
    <div class="category-tile" style="left:204px" role="img" aria-label="Category preview"><span>MASTURBA-<br>TION</span></div>
    <div class="category-tile dark" style="left:253px" role="img" aria-label="Category preview"><span>FOOT<br>FETISH</span></div>
    <div class="category-tile" style="left:302px" role="img" aria-label="Category preview"><span>LATINA</span></div>
    <div class="category-tile warm" style="left:351px" role="img" aria-label="Category preview"><span>ASIAN</span></div>
    <div class="category-tile" style="left:400px" role="img" aria-label="Category preview"><span>ASIAN</span></div>
    <div class="category-tile dark" style="left:449px" role="img" aria-label="Category preview"><span>ASIAN</span></div>
    <div class="category-tile" style="left:498px" role="img" aria-label="Category preview"><span>ASIAN</span></div>
    <svg class="strip-next" width="10" height="16" viewBox="0 0 10 16"><path d="M1 1 9 8 1 15Z" fill="#bbb"/></svg>
  </div>
</header>

<main>
  <section class="panel featured-top">
    <h2 class="panel-title" style="top:17px">Featured Videos/Ads</h2>
    <svg class="arrow" style="left:-8px;top:84px" viewBox="0 0 16 28"><path d="M14 2 3 14 14 26" fill="none" stroke="#555" stroke-width="4"/></svg>
    <svg class="arrow" style="left:652px;top:84px" viewBox="0 0 16 28"><path d="M2 2 13 14 2 26" fill="none" stroke="#555" stroke-width="4"/></svg>
    <div class="row" style="left:27px;top:37px">
      <div class="thumb embrace" role="img" aria-label="Featured video preview"><svg class="play" viewBox="0 0 22 24"><path d="M2 1 21 12 2 23Z" fill="#fff"/></svg></div>
      <div class="thumb night" role="img" aria-label="Featured video preview"><svg class="play" viewBox="0 0 22 24"><path d="M2 1 21 12 2 23Z" fill="#fff"/></svg></div>
      <div class="thumb close" role="img" aria-label="Featured video preview"><svg class="play" viewBox="0 0 22 24"><path d="M2 1 21 12 2 23Z" fill="#fff"/></svg></div>
      <div class="thumb beach" role="img" aria-label="Featured video preview, hovered"><svg class="play" viewBox="0 0 22 24"><path d="M2 1 21 12 2 23Z" fill="var(--accent)"/></svg><span class="play-label">PLAY VIDEO</span></div>
      <div class="thumb embrace" role="img" aria-label="Featured video preview"><svg class="play" viewBox="0 0 22 24"><path d="M2 1 21 12 2 23Z" fill="#fff"/></svg></div>
    </div>
  </section>

  <section class="panel recent">
    <h2 class="panel-title" style="top:11px">Recently Added Videos</h2>

    <div class="row" style="left:45px;top:40px">
      <article class="video-card"><div class="thumb embrace" role="img" aria-label="Video preview"><svg class="play" viewBox="0 0 22 24"><path d="M2 1 21 12 2 23Z" fill="#fff"/></svg></div><p class="video-title">Title of the video first and second line...</p><p class="video-meta"><span>200 views</span><span class="likes"><i><svg width="7" height="6" viewBox="0 0 10 9"><path d="M5 9 1 5A2.4 2.4 0 0 1 5 1.6 2.4 2.4 0 0 1 9 5Z" fill="#fff"/></svg></i>15</span></p></article>
      <article class="video-card"><div class="thumb night" role="img" aria-label="Video preview"><svg class="play" viewBox="0 0 22 24"><path d="M2 1 21 12 2 23Z" fill="#fff"/></svg></div><p class="video-title">Title of the video first and second line...</p><p class="video-meta"><span>5.003 views</span><span class="likes"><i><svg width="7" height="6" viewBox="0 0 10 9"><path d="M5 9 1 5A2.4 2.4 0 0 1 5 1.6 2.4 2.4 0 0 1 9 5Z" fill="#fff"/></svg></i>243</span></p></article>
      <article class="video-card"><div class="thumb close" role="img" aria-label="Video preview"><svg class="play" viewBox="0 0 22 24"><path d="M2 1 21 12 2 23Z" fill="#fff"/></svg></div><p class="video-title">Title of the video first and second line...</p><p class="video-meta"><span>1.233 views</span><span class="likes"><i><svg width="7" height="6" viewBox="0 0 10 9"><path d="M5 9 1 5A2.4 2.4 0 0 1 5 1.6 2.4 2.4 0 0 1 9 5Z" fill="#fff"/></svg></i>175</span></p></article>
      <article class="video-card"><div class="thumb beach" role="img" aria-label="Video preview"><svg class="play" viewBox="0 0 22 24"><path d="M2 1 21 12 2 23Z" fill="#fff"/></svg></div><p class="video-title">Title of the video first and second line...</p><p class="video-meta"><span>1.233.989 views</span><span class="likes"><i><svg width="7" height="6" viewBox="0 0 10 9"><path d="M5 9 1 5A2.4 2.4 0 0 1 5 1.6 2.4 2.4 0 0 1 9 5Z" fill="#fff"/></svg></i>243</span></p></article>
      <article class="video-card"><div class="thumb embrace" role="img" aria-label="Video preview"><svg class="play" viewBox="0 0 22 24"><path d="M2 1 21 12 2 23Z" fill="#fff"/></svg></div><p class="video-title">Title of the video first and second line...</p><p class="video-meta"><span>33.989 views</span><span class="likes"><i><svg width="7" height="6" viewBox="0 0 10 9"><path d="M5 9 1 5A2.4 2.4 0 0 1 5 1.6 2.4 2.4 0 0 1 9 5Z" fill="#fff"/></svg></i>175</span></p></article>
    </div>

    <div class="row" style="left:45px;top:209px">
      <article class="video-card"><div class="thumb embrace" role="img" aria-label="Video preview"><svg class="play" viewBox="0 0 22 24"><path d="M2 1 21 12 2 23Z" fill="#fff"/></svg></div><p class="video-title">Title of the video first and second line...</p><p class="video-meta"><span>200 views</span><span class="likes"><i><svg width="7" height="6" viewBox="0 0 10 9"><path d="M5 9 1 5A2.4 2.4 0 0 1 5 1.6 2.4 2.4 0 0 1 9 5Z" fill="#fff"/></svg></i>15</span></p></article>
      <article class="video-card"><div class="thumb night" role="img" aria-label="Video preview"><svg class="play" viewBox="0 0 22 24"><path d="M2 1 21 12 2 23Z" fill="#fff"/></svg></div><p class="video-title">Title of the video first and second line...</p><p class="video-meta"><span>5.003 views</span><span class="likes"><i><svg width="7" height="6" viewBox="0 0 10 9"><path d="M5 9 1 5A2.4 2.4 0 0 1 5 1.6 2.4 2.4 0 0 1 9 5Z" fill="#fff"/></svg></i>243</span></p></article>
      <article class="video-card"><div class="thumb close" role="img" aria-label="Video preview"><svg class="play" viewBox="0 0 22 24"><path d="M2 1 21 12 2 23Z" fill="#fff"/></svg></div><p class="video-title">Title of the video first and second line...</p><p class="video-meta"><span>1.233 views</span><span class="likes"><i><svg width="7" height="6" viewBox="0 0 10 9"><path d="M5 9 1 5A2.4 2.4 0 0 1 5 1.6 2.4 2.4 0 0 1 9 5Z" fill="#fff"/></svg></i>175</span></p></article>
      <article class="video-card"><div class="thumb beach" role="img" aria-label="Video preview"><svg class="play" viewBox="0 0 22 24"><path d="M2 1 21 12 2 23Z" fill="#fff"/></svg></div><p class="video-title">Title of the video first and second line...</p><p class="video-meta"><span>1.233.989 views</span><span class="likes"><i><svg width="7" height="6" viewBox="0 0 10 9"><path d="M5 9 1 5A2.4 2.4 0 0 1 5 1.6 2.4 2.4 0 0 1 9 5Z" fill="#fff"/></svg></i>243</span></p></article>
      <article class="video-card"><div class="thumb embrace" role="img" aria-label="Video preview"><svg class="play" viewBox="0 0 22 24"><path d="M2 1 21 12 2 23Z" fill="#fff"/></svg></div><p class="video-title">Title of the video first and second line...</p><p class="video-meta"><span>33.989 views</span><span class="likes"><i><svg width="7" height="6" viewBox="0 0 10 9"><path d="M5 9 1 5A2.4 2.4 0 0 1 5 1.6 2.4 2.4 0 0 1 9 5Z" fill="#fff"/></svg></i>175</span></p></article>
    </div>

    <div class="row" style="left:45px;top:378px">
      <article class="video-card"><div class="thumb embrace" role="img" aria-label="Video preview"><svg class="play" viewBox="0 0 22 24"><path d="M2 1 21 12 2 23Z" fill="#fff"/></svg></div><p class="video-title">Title of the video first and second line...</p><p class="video-meta"><span>200 views</span><span class="likes"><i><svg width="7" height="6" viewBox="0 0 10 9"><path d="M5 9 1 5A2.4 2.4 0 0 1 5 1.6 2.4 2.4 0 0 1 9 5Z" fill="#fff"/></svg></i>15</span></p></article>
      <article class="video-card"><div class="thumb night" role="img" aria-label="Video preview"><svg class="play" viewBox="0 0 22 24"><path d="M2 1 21 12 2 23Z" fill="#fff"/></svg></div><p class="video-title">Title of the video first and second line...</p><p class="video-meta"><span>5.003 views</span><span class="likes"><i><svg width="7" height="6" viewBox="0 0 10 9"><path d="M5 9 1 5A2.4 2.4 0 0 1 5 1.6 2.4 2.4 0 0 1 9 5Z" fill="#fff"/></svg></i>243</span></p></article>
      <article class="video-card"><div class="thumb close" role="img" aria-label="Video preview"><svg class="play" viewBox="0 0 22 24"><path d="M2 1 21 12 2 23Z" fill="#fff"/></svg></div><p class="video-title">Title of the video first and second line...</p><p class="video-meta"><span>1.233 views</span><span class="likes"><i><svg width="7" height="6" viewBox="0 0 10 9"><path d="M5 9 1 5A2.4 2.4 0 0 1 5 1.6 2.4 2.4 0 0 1 9 5Z" fill="#fff"/></svg></i>175</span></p></article>
      <article class="video-card"><div class="thumb beach" role="img" aria-label="Video preview"><svg class="play" viewBox="0 0 22 24"><path d="M2 1 21 12 2 23Z" fill="#fff"/></svg></div><p class="video-title">Title of the video first and second line...</p><p class="video-meta"><span>1.233.989 views</span><span class="likes"><i><svg width="7" height="6" viewBox="0 0 10 9"><path d="M5 9 1 5A2.4 2.4 0 0 1 5 1.6 2.4 2.4 0 0 1 9 5Z" fill="#fff"/></svg></i>243</span></p></article>
      <article class="video-card"><div class="thumb embrace" role="img" aria-label="Video preview"><svg class="play" viewBox="0 0 22 24"><path d="M2 1 21 12 2 23Z" fill="#fff"/></svg></div><p class="video-title">Title of the video first and second line...</p><p class="video-meta"><span>33.989 views</span><span class="likes"><i><svg width="7" height="6" viewBox="0 0 10 9"><path d="M5 9 1 5A2.4 2.4 0 0 1 5 1.6 2.4 2.4 0 0 1 9 5Z" fill="#fff"/></svg></i>175</span></p></article>
    </div>
  </section>

  <nav class="pagination" aria-label="Pages">
    <span class="current">1</span><span>2</span><span>3</span><span>4</span><span>5</span><span>6</span><span>7</span>
    <span class="gap">... ... ...</span><span>9</span>
    <span><svg width="8" height="9" viewBox="0 0 8 9"><path d="M1 0 8 4.5 1 9Z" fill="#eee"/></svg></span>
  </nav>

  <section class="panel featured-bottom">
    <h2 class="panel-title" style="top:16px">Featured Videos/Ads</h2>
    <svg class="arrow" style="left:-8px;top:84px" viewBox="0 0 16 28"><path d="M14 2 3 14 14 26" fill="none" stroke="#555" stroke-width="4"/></svg>
    <svg class="arrow" style="left:652px;top:84px" viewBox="0 0 16 28"><path d="M2 2 13 14 2 26" fill="none" stroke="#555" stroke-width="4"/></svg>
    <div class="row" style="left:27px;top:40px">
      <div class="thumb embrace" role="img" aria-label="Featured video preview"><svg class="play" viewBox="0 0 22 24"><path d="M2 1 21 12 2 23Z" fill="#fff"/></svg></div>
      <div class="thumb night" role="img" aria-label="Featured video preview"><svg class="play" viewBox="0 0 22 24"><path d="M2 1 21 12 2 23Z" fill="#fff"/></svg></div>
      <div class="thumb close" role="img" aria-label="Featured video preview"><svg class="play" viewBox="0 0 22 24"><path d="M2 1 21 12 2 23Z" fill="#fff"/></svg></div>
      <div class="thumb beach" role="img" aria-label="Featured video preview"><svg class="play" viewBox="0 0 22 24"><path d="M2 1 21 12 2 23Z" fill="#fff"/></svg></div>
      <div class="thumb embrace" role="img" aria-label="Featured video preview"><svg class="play" viewBox="0 0 22 24"><path d="M2 1 21 12 2 23Z" fill="#fff"/></svg></div>
    </div>
  </section>
</main>

<footer class="site-footer">
  <div class="footer-col" style="left:172px"><h4>INFORMATION</h4>information<br>information<br>information<br>information</div>
  <div class="footer-col" style="left:296px"><h4>SUPPORT</h4>support<br>support<br>support<br>support</div>
  <div class="footer-col" style="left:420px"><h4>OUR TEAM</h4>our team<br>our team<br>our team<br>our team</div>
  <div class="footer-col" style="left:545px"><h4>OTHER MENU</h4>other menu<br>other menu<br>other menu<br>other menu</div>
  <div class="footer-col" style="left:670px"><h4>OTHER MENU</h4>other menu<br>other menu<br>other menu<br>other menu</div>
  <p class="copyright">© VELVETREEL.COM, 2014</p>
</footer>

</body>
</html>
```